Identity Package (Logo, Website)

We need a logo and website design for a new company.
The new company is a voicemail transcription service provider. It's name is KB7LUX.io
It will be very transactional. We like the "bootstrap" look and feel, and will be using a developer familiar with bootstrap. Here are the kinds of webpages we like :
https://www.plinverotrack.io
http://www.quorvix.com/
http://www.brenmoda.com/
There will only be 5 pages, as follows :
1- Homepage
2- Voicemail Transcription for Individuals
3- Voicemail Transcription for Companies
4- Wholesale Voicemail Transcription for Service Providers/Enterprises
5- Contact us
As far as the logo is concerned, we'd like to have just stylized text. It should be done in such a way as to make it easy to see the different elements of the name, which are KB, 7, and LUX.
Reason: I have received a number of designs, but the designs are mostly from the same few designers (not that much variety in designers). I'd like a few more to compare if possible, so I thought I would keep this open until Monday to give more designers the opportunity to submit over the weekend. Thanks!

```html
<!DOCTYPE html>
<html lang="en">
<head>
<meta charset="utf-8">
<title>KB7LUX.io – Convert Voicemail to Text</title>
<link rel="stylesheet" href="https://fonts.googleapis.com/css2?family=Nunito+Sans:wght@400;600;700&family=Arimo:wght@400;700&display=swap">
<style>
  :root {
    --brand-blue: #1273b0;
    --title-blue: #1c74b2;
    --icon-grey: #48484a;
    --icon-grey-soft: #5a5a5c;
    --header-bg: #f9f9f9;
    --hero-top: #f4f4f4;
    --hero-bottom: #cdcdcf;
    --button-green: #77bd57;
    --ink: #111111;
    --white: #ffffff;
    --footer-bg: #fafafa;
    --rule: #e2e2e2;
  }
  * { box-sizing: border-box; margin: 0; padding: 0; }
  html, body { width: 1200px; height: 816px; overflow: hidden; }
  body {
    position: relative;
    font-family: "Nunito Sans", sans-serif;
    background: var(--footer-bg);
    color: var(--ink);
  }

  /* Header */
  .site-header {
    position: absolute; left: 0; top: 0; width: 1200px; height: 102px;
    background: var(--header-bg);
    border-bottom: 1px solid var(--rule);
  }
  .brand {
    position: absolute; left: 64px; top: 30px;
    display: flex; align-items: center; gap: 12px;
    font-family: "Nunito Sans", sans-serif; font-weight: 600;
    font-size: 42px; color: var(--brand-blue); letter-spacing: 1px;
  }
  .brand-mark { width: 16px; height: 16px; background: var(--brand-blue); }
  .main-nav { position: absolute; top: 50px; left: 0; width: 100%; }
  .main-nav a {
    position: absolute; font-family: "Arimo", sans-serif; font-size: 15px;
    color: var(--ink); text-decoration: none; white-space: nowrap;
  }
  .nav-home { left: 785px; }
  .nav-services { left: 873px; }
  .nav-contact { left: 1075px; }

  /* Hero */
  .hero {
    position: absolute; left: 0; top: 102px; width: 1200px; height: 381px;
    background: linear-gradient(to bottom, var(--hero-top) 0%, var(--hero-top) 45%, var(--hero-bottom) 100%);
  }
  .hero-title {
    position: absolute; left: 0; top: 36px; width: 1286px; text-align: center;
    font-weight: 400; font-size: 54px; color: var(--title-blue);
  }
  .hero-art {
    position: absolute; border-radius: 10px;
    background: linear-gradient(to bottom, var(--icon-grey-soft), var(--icon-grey));
  }
  .art-voicemail { left: 246px; top: 128px; width: 191px; height: 158px; }
  .art-message { left: 820px; top: 123px; width: 162px; height: 162px; }
  .hero-arrow { position: absolute; left: 526px; top: 178px; }
  .cta-button {
    position: absolute; left: 573px; top: 308px; width: 125px; height: 43px;
    background: var(--button-green); border-radius: 3px;
    display: flex; align-items: center; justify-content: center;
    font-weight: 700; font-size: 16px; color: var(--ink); text-decoration: none;
  }

  /* Audience band */
  .audiences {
    position: absolute; left: 0; top: 483px; width: 1200px; height: 274px;
    background: var(--brand-blue); color: var(--white);
  }
  .audiences-title {
    position: absolute; left: 0; top: 29px; width: 100%; text-align: center;
    font-weight: 600; font-size: 35px;
  }
  .audience { position: absolute; top: 98px; width: 300px; height: 150px; }
  .audience-individual { left: 83px; }
  .audience-companies { left: 471px; }
  .audience-enterprise { left: 884px; }
  .audience-name {
    display: flex; align-items: center; gap: 8px;
    font-weight: 400; font-size: 28px; line-height: 1; height: 34px;
  }
  .audience-name svg { flex: none; }
  .audience-text {
    margin-top: 10px; width: 240px;
    font-size: 14px; line-height: 16.4px; letter-spacing: 0.3px;
  }
  .audience-text .line { display: block; text-align: justify; text-align-last: justify; white-space: nowrap; }
  .audience-text .line-last { text-align-last: left; }
  .learn-more {
    position: absolute; top: 127px; font-size: 16px; color: var(--ink);
    text-decoration: none; white-space: nowrap;
  }
  .audience-individual .learn-more { left: 164px; }
  .audience-companies .learn-more { left: 151px; }
  .audience-enterprise .learn-more { left: 130px; }

  /* Footer */
  .site-footer {
    position: absolute; left: 0; top: 757px; width: 1200px; height: 59px;
    background: var(--footer-bg);
  }
  .copyright {
    position: absolute; right: 62px; top: 10px;
    font-weight: 700; font-size: 15px; color: var(--ink);
  }
</style>
</head>
<body>
  <header class="site-header">
    <div class="brand"><span class="brand-mark"></span>KB7LUX</div>
    <nav class="main-nav">
      <a class="nav-home" href="#">Home</a>
      <a class="nav-services" href="#">Transcription Services</a>
      <a class="nav-contact" href="#">Contact</a>
    </nav>
  </header>

  <section class="hero">
    <h1 class="hero-title">Convert Voicemail to Text</h1>
    <div class="hero-art art-voicemail" role="img" aria-label="Illustration of a voicemail speech bubble"></div>
    <svg class="hero-arrow" width="200" height="30" viewBox="0 0 200 30" aria-hidden="true">
      <rect x="0" y="10" width="170" height="10" fill="var(--icon-grey)"/>
      <polygon points="166,2 196,15 166,28" fill="var(--icon-grey)"/>
    </svg>
    <div class="hero-art art-message" role="img" aria-label="Illustration of an open envelope holding a text message"></div>
    <a class="cta-button" href="#">Know more</a>
  </section>

  <section class="audiences">
    <h2 class="audiences-title">We provide Voicemail transcription to</h2>

    <article class="audience audience-individual">
      <h3 class="audience-name">
        <svg width="22" height="32" viewBox="0 0 22 32" aria-hidden="true"><circle cx="11" cy="7" r="7" fill="var(--white)"/><rect x="0" y="16" width="22" height="16" rx="4" fill="var(--white)"/></svg>
        Individual
      </h3>
      <p class="audience-text"><span class="line">Usce euismod consequat ante.</span><span class="line">Lorem ipsum dolor sit amet,</span><span class="line">consectetuer adipiscig elit.</span><span class="line line-last">Pellentesque sed dolor.</span></p>
      <a class="learn-more" href="#">Learn more</a>
    </article>

    <article class="audience audience-companies">
      <h3 class="audience-name">
        <svg width="24" height="28" viewBox="0 0 24 28" aria-hidden="true"><path d="M0 0 h12 v28 h-12 z M13 8 h11 v20 h-11 z" fill="var(--white)"/><g fill="var(--brand-blue)"><rect x="2" y="3" width="3" height="3"/><rect x="7" y="3" width="3" height="3"/><rect x="2" y="9" width="3" height="3"/><rect x="7" y="9" width="3" height="3"/><rect x="2" y="15" width="3" height="3"/><rect x="7" y="15" width="3" height="3"/><rect x="16" y="12" width="5" height="3"/><rect x="16" y="18" width="5" height="3"/><rect x="4" y="22" width="4" height="6"/></g></svg>
        Companies
      </h3>
      <p class="audience-text"><span class="line">Usce euismod consequat ante.</span><span class="line">Lorem ipsum dolor sit amet,</span><span class="line">consectetuer adipiscig elit.</span><span class="line line-last">Pellentesque sed dolor.</span></p>
      <a class="learn-more" href="#">Learn more</a>
    </article>

    <article class="audience audience-enterprise">
      <h3 class="audience-name">
        <svg width="28" height="32" viewBox="0 0 28 32" aria-hidden="true"><g fill="var(--white)"><ellipse cx="14" cy="5" rx="14" ry="5"/><path d="M0 9 q14 8 28 0 v6 q-14 8 -28 0 z"/><path d="M0 18 q14 8 28 0 v6 q-14 8 -28 0 z"/></g></svg>
        Enterprise
      </h3>
      <p class="audience-text"><span class="line">Usce euismod consequat ante.</span><span class="line">Lorem ipsum dolor sit amet,</span><span class="line">consectetuer adipiscig elit.</span><span class="line line-last">Pellentesque sed dolor.</span></p>
      <a class="learn-more" href="#">Learn more</a>
    </article>
  </section>

  <footer class="site-footer">
    <p class="copyright">Copyright 2014 KB7LUX.</p>
  </footer>
</body>
</html>
```